Business Cards

Simple but professional looking business cards

Name: Rina Tolvardi
Title: Principle Ledger Systems Applications Consultant
Email: r@kbrx.net.au
web : www.kbrx.net.au
Phone: +61.8.95203417
Mobile: +61.431862055
Updates

Hi All, Please include the office address Level 1, 200 Quarrington St, West Perth, WA, 6005

Industry/Entity Type

Business

```html
<!DOCTYPE html>
<html lang="en">
<head>
<meta charset="utf-8">
<title>KBRX Business Cards</title>
<link rel="stylesheet" href="https://fonts.googleapis.com/css2?family=Arimo:wght@400;700&family=Cinzel:wght@600&display=swap">
<style>
  :root {
    --bg: #e9e6e2;
    --paper: #ffffff;
    --green: #8cc84b;
    --blue: #1a72bb;
    --navy: #2a4e9a;
    --ink: #1b1b1b;
    --badge: #e5262f;
  }
  * { margin: 0; padding: 0; box-sizing: border-box; }
  html, body { width: 1200px; height: 914px; overflow: hidden; }
  body {
    background: var(--bg);
    font-family: "Arimo", Arial, sans-serif;
    color: var(--ink);
    position: relative;
  }
  .card {
    position: absolute;
    left: 320px;
    width: 560px;
    height: 320px;
    background: var(--paper);
    box-shadow: 0 6px 18px rgba(0,0,0,0.15);
    overflow: hidden;
  }
  .card--back { top: 100px; }
  .card--front { top: 494px; }

  .stripe { position: absolute; left: 0; right: 0; height: 8px; display: flex; }
  .stripe--top { top: 0; }
  .stripe--bottom { bottom: 0; }
  .stripe__green { width: 34%; background: var(--green); }
  .stripe__blue { flex: 1; background: var(--blue); }

  .brand { display: flex; align-items: center; gap: 10px; }
  .brand__dot { width: 18px; height: 18px; border-radius: 50%; background: var(--green); }
  .brand__name {
    font-family: "Arimo", Arial, sans-serif;
    font-weight: 700;
    color: var(--blue);
    letter-spacing: 1px;
  }
  .card--back .brand { position: absolute; left: 60px; top: 92px; }
  .card--back .brand__name { font-size: 78px; }
  .card--back .brand__dot { width: 34px; height: 34px; }

  .partner {
    position: absolute;
    right: 70px; bottom: 50px;
    display: flex; align-items: center; gap: 8px;
  }
  .partner__badge { width: 108px; height: 30px; background: var(--badge); }
  .partner__label {
    font-size: 13px; font-weight: 700; line-height: 15px;
  }

  .band { position: absolute; top: 0; bottom: 0; width: 14px; display: flex; flex-direction: column; }
  .band--left { left: 0; }
  .band--right { right: 0; }
  .band__green { flex: 1; background: var(--green); }
  .band__navy { flex: 1; background: var(--navy); }

  .card--front .content {
    position: absolute;
    left: 14px; right: 14px; top: 30px;
    display: flex; flex-direction: column; align-items: center;
  }
  .card--front .brand__name { font-size: 44px; }
  .person-name {
    margin-top: 10px;
    font-family: "Cinzel", Georgia, serif;
    font-weight: 600;
    font-size: 20px;
    letter-spacing: 1px;
  }
  .person-title { font-size: 16px; margin-top: 2px; }
  .contact { list-style: none; margin-top: 20px; }
  .contact li {
    display: flex; align-items: center; gap: 8px;
    font-size: 15px; line-height: 21px;
  }
  .contact svg { width: 12px; height: 12px; fill: var(--ink); flex: none; }
</style>
</head>
<body>
  <section class="card card--back" aria-label="Card back">
    <div class="stripe stripe--top"><span class="stripe__green"></span><span class="stripe__blue"></span></div>
    <div class="brand">
      <span class="brand__dot"></span>
      <span class="brand__name">KBRX</span>
    </div>
    <div class="partner">
      <div class="partner__badge" aria-label="Partner badge"></div>
      <p class="partner__label">Gold<br>Partner</p>
    </div>
    <div class="stripe stripe--bottom"><span class="stripe__green"></span><span class="stripe__blue"></span></div>
  </section>

  <section class="card card--front" aria-label="Card front">
    <div class="band band--left"><span class="band__green"></span><span class="band__navy"></span></div>
    <div class="band band--right"><span class="band__green"></span><span class="band__navy"></span></div>
    <div class="content">
      <div class="brand">
        <span class="brand__dot"></span>
        <span class="brand__name">KBRX</span>
      </div>
      <h1 class="person-name">Rina Tolvardi</h1>
      <p class="person-title">Principle Ledger Systems Applications Consultant</p>
      <ul class="contact">
        <li><svg viewBox="0 0 12 12" aria-hidden="true"><path d="M2.5 1l2 2-1 1.5c.8 1.6 1.9 2.7 3.5 3.5L8.5 7l2 2-1.5 2C5 11 1 7 1 2.5z"/></svg>+61.8.95203417</li>
        <li><svg viewBox="0 0 12 12" aria-hidden="true"><rect x="3" y="0.5" width="6" height="11" rx="1"/><rect x="4" y="2" width="4" height="6" fill="#fff"/></svg>+61.431862055</li>
        <li><svg viewBox="0 0 12 12" aria-hidden="true"><rect x="0.5" y="2.5" width="11" height="7"/><path d="M0.5 2.5L6 7l5.5-4.5" stroke="#fff" fill="none"/></svg>r@kbrx.net.au</li>
        <li><svg viewBox="0 0 12 12" aria-hidden="true"><circle cx="6" cy="6" r="5.5"/><path d="M0.5 6h11M6 .5v11" stroke="#fff"/></svg>www.kbrx.net.au</li>
        <li><svg viewBox="0 0 12 12" aria-hidden="true"><path d="M6 .5a4 4 0 0 1 4 4c0 3-4 7-4 7s-4-4-4-7a4 4 0 0 1 4-4z"/><circle cx="6" cy="4.5" r="1.4" fill="#fff"/></svg>Level 1, 200 Quarrington St,</li>
      </ul>
    </div>
  </section>
</body>
</html>
```